Landcape Construction Company needs a flyer to catch attention

A flyer that can be displayed at several different stores detailing our skills, work produced, experience and contact details. Information can be extracted from our website www.brvkw.co.nz. The flyer should feel very green, with addition of pics of work completed as well as stock images of lush green plants, lawns, landscape or similar. Needs to be eye catching with just enough information to express our experience and commitment to high standards

Target Market(s)

Residential
Landscape Architects

Industry/Entity Type

Landscaping

Font styles to use
Serif

Colors
abd037

Requirements
Must have
• Our logo
Experience
Services offered including pictures
All information avail on our website www.brvkw.co.nz
Nice to have
• stock images of lush greenery like a garden after fresh rainfall
Should not have
• Nothing comes to mind

```html
<!DOCTYPE html>
<html lang="en">
<head>
<meta charset="utf-8">
<title>Brookvale Landworks Flyer</title>
<link href="https://fonts.googleapis.com/css2?family=Poppins:wght@300;400;500;600;700;800&display=swap" rel="stylesheet">
<style>
  :root{
    --lime:#abd037;
    --lime-bright:#8cc63f;
    --green-dark:#0e5e2c;
    --green-mid:#1f7a3a;
    --green-panel:#2a8a46;
    --pale:#e3eed6;
    --white:#ffffff;
    --ink:#1c3a22;
    --page:#8d9396;
  }
  *{margin:0;padding:0;box-sizing:border-box}
  html,body{width:697px;height:1200px;overflow:hidden;background:var(--page);font-family:"Poppins",sans-serif}
  .stage{position:relative;width:697px;height:1200px}
  .flyer{position:absolute;left:10px;top:121px;width:880px;height:1245px;transform:scale(0.769);transform-origin:0 0;overflow:hidden;background:var(--pale);box-shadow:0 6px 18px rgba(0,0,0,.35)}
  .art{position:absolute;inset:0}
  .brand{position:absolute;left:20px;top:30px;width:280px;text-align:center;color:var(--white)}
  .brand-mark{width:140px;height:140px;border-radius:50%;background:var(--lime-bright);margin:0 auto 12px}
  .brand-name{font-weight:500;font-size:22px;line-height:1.15;padding:0 40px}
  .experience{position:absolute;left:58px;top:320px;width:198px;text-align:center;color:var(--white);border-top:2px solid var(--white);border-bottom:2px solid var(--white);padding:8px 0 10px}
  .experience .small{font-size:16px;font-weight:500;line-height:1.2}
  .experience .big{font-size:40px;font-weight:800;line-height:1.05}
  .headline{position:absolute;left:477px;top:312px;color:var(--white)}
  .headline .l1{font-size:24px;font-weight:700;letter-spacing:.2px}
  .headline .l2{font-size:47px;font-weight:800;color:var(--lime-bright);line-height:1;margin-top:2px}
  .headline .l3{font-size:30px;font-weight:700;line-height:1.2}
  .headline .l3 span{font-weight:300}
  .headline .rule{width:116px;height:4px;background:var(--lime-bright);margin-top:8px}
  .services{position:absolute;left:597px;top:505px;width:248px;height:592px;background:var(--green-panel);padding:22px 26px;color:var(--white)}
  .services h2{font-size:27px;font-weight:700;display:inline-block;border-bottom:4px solid var(--lime-bright);padding-bottom:2px;margin-bottom:26px}
  .services ul{list-style:none}
  .services li{display:flex;align-items:center;gap:8px;font-size:14px;font-weight:500;height:29.6px}
  .services li.gap{margin-top:17px}
  .tick{width:17px;height:17px;flex:none}
  .about{position:absolute;left:32px;top:593px;width:522px;color:var(--ink);font-size:11.6px;line-height:1.24;text-align:justify}
  .about p{margin-bottom:13px}
  .about .lead{color:var(--green-mid);font-weight:600}
  .projects{position:absolute;left:32px;top:810px;width:520px}
  .projects h2{font-size:27px;font-weight:700;color:var(--green-mid);display:inline-block;border-bottom:3px solid var(--lime-bright);padding-bottom:2px}
  .projects ul{list-style:none;display:grid;grid-template-columns:147px 147px 200px;row-gap:14px;margin-top:30px}
  .projects li{display:flex;align-items:center;gap:9px;font-size:11.5px;font-weight:600;color:var(--ink)}
  .projects .tick{width:22px;height:22px}
  .web{position:absolute;left:82px;top:1180px;width:354px;height:27px;background:var(--lime-bright);color:var(--white);font-size:15px;letter-spacing:7px;text-align:center;line-height:27px}
  .call{position:absolute;left:597px;top:1140px;color:var(--white)}
  .call .cta{font-size:17px;font-weight:700;color:var(--lime-bright)}
  .call .phone{font-size:41px;font-weight:700;line-height:1.1}
</style>
</head>
<body>
<div class="stage">
  <div class="flyer">
    <svg class="art" viewBox="0 0 880 1245" xmlns="http://www.w3.org/2000/svg">
      <defs>
        <linearGradient id="gardenTopGrad" x1="0" y1="0" x2="0.3" y2="1">
          <stop offset="0" stop-color="#1f6b35"/><stop offset=".3" stop-color="#175f2d"/><stop offset=".55" stop-color="#1e7436"/><stop offset=".8" stop-color="#2a8a3c"/><stop offset="1" stop-color="#1d6f33"/>
        </linearGradient>
        <linearGradient id="siteGrad" x1="0" y1="0" x2="0" y2="1">
          <stop offset="0" stop-color="#f2b35e"/><stop offset=".12" stop-color="#d99250"/><stop offset=".26" stop-color="#5a5237"/><stop offset=".42" stop-color="#34402e"/><stop offset=".6" stop-color="#5d5a52"/><stop offset=".8" stop-color="#6e6d68"/><stop offset="1" stop-color="#454644"/>
        </linearGradient>
        <linearGradient id="lowerGardenGrad" x1="0" y1="0" x2="0" y2="1">
          <stop offset="0" stop-color="#e3eed6" stop-opacity="0"/><stop offset=".25" stop-color="#7fae5a"/><stop offset=".5" stop-color="#3f7d32"/><stop offset=".75" stop-color="#2f6a2a"/><stop offset="1" stop-color="#6b7a5a"/>
        </linearGradient>
        <linearGradient id="proj1" x1="0" y1="0" x2="1" y2="1">
          <stop offset="0" stop-color="#8b5a3a"/><stop offset=".3" stop-color="#b9b6ac"/><stop offset=".55" stop-color="#6fb83e"/><stop offset=".8" stop-color="#4c9a2e"/><stop offset="1" stop-color="#2c3a2a"/>
        </linearGradient>
        <linearGradient id="proj2" x1="0" y1="0" x2="1" y2="1">
          <stop offset="0" stop-color="#2f4a2c"/><stop offset=".35" stop-color="#7d7c76"/><stop offset=".7" stop-color="#a38451"/><stop offset="1" stop-color="#5c5a55"/>
        </linearGradient>
        <linearGradient id="proj3" x1="0" y1="0" x2="1" y2="1">
          <stop offset="0" stop-color="#4d7f8f"/><stop offset=".3" stop-color="#8aa7ab"/><stop offset=".6" stop-color="#8f8e8a"/><stop offset="1" stop-color="#6c6b68"/>
        </linearGradient>
        <clipPath id="bigCircle"><circle cx="670" cy="250" r="318"/></clipPath>
      </defs>
      <rect width="880" height="560" fill="url(#gardenTopGrad)" role="img" aria-label="Photo of a green lawn and garden in front of a house, tinted green"/>
      <polygon points="0,560 0,420 330,470 600,560" fill="#0f5a2a"/>
      <rect y="900" width="880" height="345" fill="url(#lowerGardenGrad)" role="img" aria-label="Photo of a finished garden with hedges, lawn and timber decking"/>
      <path d="M430 560 Q700 600 880 505 L880 540 Q720 620 470 585 Z" fill="var(--lime-bright)"/>
      <path d="M380 560 Q680 585 880 480 L880 512 Q700 605 430 568 Z" fill="#17703a"/>
      <circle cx="670" cy="250" r="352" fill="var(--lime-bright)"/>
      <circle cx="670" cy="250" r="336" fill="#1a7a3a"/>
      <rect x="0" y="0" width="880" height="560" fill="url(#siteGrad)" clip-path="url(#bigCircle)" role="img" aria-label="Photo of a paving machine laying pavers on a site at sunset"/>
      <g stroke="var(--lime-bright)" stroke-width="5">
        <circle cx="103" cy="1030" r="76" fill="url(#proj1)" role="img" aria-label="Project photo: paved path beside lawn"/>
        <circle cx="270" cy="1030" r="76" fill="url(#proj2)" role="img" aria-label="Project photo: courtyard with timber seating"/>
        <circle cx="437" cy="1030" r="76" fill="url(#proj3)" role="img" aria-label="Project photo: decking beside a pool"/>
      </g>
    </svg>

    <div class="brand">
      <div class="brand-mark"></div>
      <div class="brand-name">Brookvale Landworks Ltd</div>
    </div>

    <div class="experience">
      <div class="small">With more than</div>
      <div class="big">25 YEARS</div>
      <div class="small">experience in the<br>landscaping industry</div>
    </div>

    <div class="headline">
      <div class="l1">RESIDENTIAL &amp; COMMERCIAL</div>
      <div class="l2">LANDSCAPING</div>
      <div class="l3">BASED IN <span>CANTERBURY</span></div>
      <div class="rule"></div>
    </div>

    <section class="about">
      <p class="lead">Our company is built on honesty, teamwork, sound knowledge and a determination to provide our customers with the highest quality product and service. We are a small team of highly skilled, dedicated and reliable professionals who complete projects efficiently and with outstanding workmanship.</p>
      <p>We hold Pavecor Pro Accreditation status making us preferred installers of this paving system. To achieve this we had to show we had a solid understanding of the system and the skill set to ensure workmanship was held to the highest standard.</p>
      <p>How we work is simple. We will listen, get a clear idea of your vision and offer practical advice in order to achieve the best outcome within your budget and scope. An initial consultation is free so give us a call and let's chat about getting the best solution to your landscaping needs.</p>
    </section>

    <section class="projects">
      <h2>OUR PROJECTS</h2>
      <ul>
        <li><svg class="tick" viewBox="0 0 20 20"><circle cx="10" cy="10" r="9" fill="var(--lime-bright)"/><path d="M6 10l3 3 5-6" stroke="#fff" stroke-width="2" fill="none"/></svg>STREETSCAPES</li>
        <li><svg class="tick" viewBox="0 0 20 20"><circle cx="10" cy="10" r="9" fill="var(--lime-bright)"/><path d="M6 10l3 3 5-6" stroke="#fff" stroke-width="2" fill="none"/></svg>NEWBURY</li>
        <li><svg class="tick" viewBox="0 0 20 20"><circle cx="10" cy="10" r="9" fill="var(--lime-bright)"/><path d="M6 10l3 3 5-6" stroke="#fff" stroke-width="2" fill="none"/></svg>RANGIORA PROJECT</li>
        <li><svg class="tick" viewBox="0 0 20 20"><circle cx="10" cy="10" r="9" fill="var(--lime-bright)"/><path d="M6 10l3 3 5-6" stroke="#fff" stroke-width="2" fill="none"/></svg>HARWOODS</li>
        <li><svg class="tick" viewBox="0 0 20 20"><circle cx="10" cy="10" r="9" fill="var(--lime-bright)"/><path d="M6 10l3 3 5-6" stroke="#fff" stroke-width="2" fill="none"/></svg>MAPLE PLACE</li>
        <li><svg class="tick" viewBox="0 0 20 20"><circle cx="10" cy="10" r="9" fill="var(--lime-bright)"/><path d="M6 10l3 3 5-6" stroke="#fff" stroke-width="2" fill="none"/></svg>KESTREL STREET &amp; MORE</li>
      </ul>
    </section>

    <section class="services">
      <h2>SERVICES</h2>
      <ul>
        <li><svg class="tick" viewBox="0 0 20 20"><circle cx="10" cy="10" r="8" fill="none" stroke="#fff" stroke-width="2"/><path d="M6 10l3 3 5-6" stroke="#fff" stroke-width="2" fill="none"/></svg>PATIOS</li>
        <li><svg class="tick" viewBox="0 0 20 20"><circle cx="10" cy="10" r="8" fill="none" stroke="#fff" stroke-width="2"/><path d="M6 10l3 3 5-6" stroke="#fff" stroke-width="2" fill="none"/></svg>PAVING</li>
        <li><svg class="tick" viewBox="0 0 20 20"><circle cx="10" cy="10" r="8" fill="none" stroke="#fff" stroke-width="2"/><path d="M6 10l3 3 5-6" stroke="#fff" stroke-width="2" fill="none"/></svg>CONCRETE</li>
        <li><svg class="tick" viewBox="0 0 20 20"><circle cx="10" cy="10" r="8" fill="none" stroke="#fff" stroke-width="2"/><path d="M6 10l3 3 5-6" stroke="#fff" stroke-width="2" fill="none"/></svg>WATER FEATURES</li>
        <li><svg class="tick" viewBox="0 0 20 20"><circle cx="10" cy="10" r="8" fill="none" stroke="#fff" stroke-width="2"/><path d="M6 10l3 3 5-6" stroke="#fff" stroke-width="2" fill="none"/></svg>DECKING</li>
        <li class="gap"><svg class="tick" viewBox="0 0 20 20"><circle cx="10" cy="10" r="8" fill="none" stroke="#fff" stroke-width="2"/><path d="M6 10l3 3 5-6" stroke="#fff" stroke-width="2" fill="none"/></svg>FENCING</li>
        <li><svg class="tick" viewBox="0 0 20 20"><circle cx="10" cy="10" r="8" fill="none" stroke="#fff" stroke-width="2"/><path d="M6 10l3 3 5-6" stroke="#fff" stroke-width="2" fill="none"/></svg>BOARDWALKS</li>
        <li><svg class="tick" viewBox="0 0 20 20"><circle cx="10" cy="10" r="8" fill="none" stroke="#fff" stroke-width="2"/><path d="M6 10l3 3 5-6" stroke="#fff" stroke-width="2" fill="none"/></svg>TIMBER</li>
        <li><svg class="tick" viewBox="0 0 20 20"><circle cx="10" cy="10" r="8" fill="none" stroke="#fff" stroke-width="2"/><path d="M6 10l3 3 5-6" stroke="#fff" stroke-width="2" fill="none"/></svg>PLANTER BOXES</li>
        <li><svg class="tick" viewBox="0 0 20 20"><circle cx="10" cy="10" r="8" fill="none" stroke="#fff" stroke-width="2"/><path d="M6 10l3 3 5-6" stroke="#fff" stroke-width="2" fill="none"/></svg>PERGOLAS</li>
        <li class="gap"><svg class="tick" viewBox="0 0 20 20"><circle cx="10" cy="10" r="8" fill="none" stroke="#fff" stroke-width="2"/><path d="M6 10l3 3 5-6" stroke="#fff" stroke-width="2" fill="none"/></svg>RETAINING WALLS</li>
        <li><svg class="tick" viewBox="0 0 20 20"><circle cx="10" cy="10" r="8" fill="none" stroke="#fff" stroke-width="2"/><path d="M6 10l3 3 5-6" stroke="#fff" stroke-width="2" fill="none"/></svg>GARDENS &amp; LAWNS</li>
        <li><svg class="tick" viewBox="0 0 20 20"><circle cx="10" cy="10" r="8" fill="none" stroke="#fff" stroke-width="2"/><path d="M6 10l3 3 5-6" stroke="#fff" stroke-width="2" fill="none"/></svg>IRRIGATION</li>
        <li><svg class="tick" viewBox="0 0 20 20"><circle cx="10" cy="10" r="8" fill="none" stroke="#fff" stroke-width="2"/><path d="M6 10l3 3 5-6" stroke="#fff" stroke-width="2" fill="none"/></svg>PROJECT MANAGEMENT</li>
        <li><svg class="tick" viewBox="0 0 20 20"><circle cx="10" cy="10" r="8" fill="none" stroke="#fff" stroke-width="2"/><path d="M6 10l3 3 5-6" stroke="#fff" stroke-width="2" fill="none"/></svg>CONSULTATION</li>
      </ul>
    </section>

    <div class="web">www.brvkw.co.nz</div>

    <div class="call">
      <div class="cta">CALL US TODAY!</div>
      <div class="phone">021 555 014</div>
    </div>
  </div>
</div>
</body>
</html>
```